Bright Pipe Plumbing is a family owned plumbing company on Sydney's Northern Beaches. We are looking for a catchy business card that will appeal to consumes and stick in peoples minds. Our colours are Yellow Aqua and Blues.

The design should be something that will remind the consume we are the people the call with any plumbing needs.

Target Market(s)

property owners and managers.

Industry/Entity Type

Business

Contact Information for Business Card

Bright Pipe Plumbing, Derek Fairholm, 0418 337 904, Admin@brightpipeplumbing.example, www.brightpipeplumbing.example, Plumber

```html
<!DOCTYPE html>
<html lang="en">
<head>
<meta charset="utf-8">
<title>Bright Pipe Plumbing – Business Card</title>
<link rel="stylesheet" href="https://fonts.googleapis.com/css2?family=Arimo:wght@400;700&family=Montserrat:wght@400&display=swap">
<style>
  :root {
    --page-bg: #e4e4e4;
    --ink-navy: #1f3766;
    --ink-soft: #3a4f77;
    --aqua-light: #b9e6e4;
    --aqua: #7fd0d8;
    --sky: #5fc0dc;
    --yellow-pale: #f1f3b4;
    --yellow: #e3ec8c;
    --gold: #e0b43a;
    --sea-blue: #2aa4d3;
    --sea-deep: #1f8fc4;
    --glow: #ffffff;
    --accent-ring: #3aa9b8;
  }
  * { box-sizing: border-box; margin: 0; padding: 0; }
  html, body {
    width: 1200px;
    height: 900px;
    overflow: hidden;
    background: var(--page-bg);
  }
  .stage {
    width: 1200px;
    height: 900px;
    display: flex;
    align-items: center;
    justify-content: center;
  }
  .business-card {
    position: relative;
    width: 1050px;
    height: 600px;
    overflow: hidden;
    box-shadow: 0 12px 30px rgba(0,0,0,0.18);
  }
  .card-texture {
    position: absolute;
    inset: 0;
    background:
      radial-gradient(circle at 72% 33%, var(--glow) 0, rgba(255,255,255,0.85) 8%, rgba(255,255,255,0) 22%),
      linear-gradient(180deg,
        var(--yellow-pale) 0%,
        var(--aqua-light) 14%,
        var(--aqua) 38%,
        var(--aqua-light) 56%,
        var(--sky) 68%,
        var(--yellow) 76%,
        var(--sea-blue) 84%,
        var(--sea-deep) 92%,
        var(--yellow) 100%);
  }
  .brand {
    position: absolute;
    left: 420px;
    top: 118px;
    display: flex;
    flex-direction: column;
    align-items: flex-start;
  }
  .brand-name {
    font-family: "Arimo", Arial, sans-serif;
    font-weight: 700;
    font-size: 34px;
    line-height: 40px;
    letter-spacing: 1px;
    color: var(--ink-navy);
    text-transform: uppercase;
  }
  .brand-tagline {
    margin-top: 6px;
    margin-left: 50px;
    font-family: "Arimo", Arial, sans-serif;
    font-weight: 700;
    font-size: 22px;
    line-height: 26px;
    color: var(--ink-navy);
    text-transform: uppercase;
  }
  .brand-rule {
    margin-top: 8px;
    margin-left: 50px;
    width: 190px;
    height: 5px;
    background: linear-gradient(180deg, var(--gold) 0 50%, var(--sea-blue) 50% 100%);
  }
  .brand-mark {
    position: absolute;
    left: 870px;
    top: 120px;
    width: 96px;
    height: 96px;
    border-radius: 50%;
    border: 4px solid var(--accent-ring);
  }
  .person {
    position: absolute;
    left: 60px;
    top: 224px;
  }
  .person-name {
    font-family: "Arimo", Arial, sans-serif;
    font-weight: 700;
    font-size: 40px;
    line-height: 46px;
    color: var(--ink-navy);
    text-transform: uppercase;
    letter-spacing: 0.5px;
  }
  .person-role {
    font-family: "Arimo", Arial, sans-serif;
    font-weight: 400;
    font-size: 19px;
    color: var(--ink-soft);
    margin-top: 4px;
    margin-left: 60px;
  }
  .contact-list {
    position: absolute;
    left: 470px;
    top: 340px;
    list-style: none;
    font-family: "Montserrat", Arial, sans-serif;
    font-size: 23px;
    color: var(--ink-navy);
  }
  .contact-item {
    display: flex;
    align-items: center;
    gap: 14px;
    height: 36px;
  }
  .contact-icon {
    width: 20px;
    height: 20px;
    flex: none;
  }
</style>
</head>
<body>
<main class="stage">
  <section class="business-card">
    <div class="card-texture" role="img" aria-label="Soft streaked water texture in yellow, aqua and blue with a bright glow"></div>

    <div class="brand">
      <span class="brand-name">Bright Pipe Plumbing</span>
      <span class="brand-tagline">Water Drainage &amp; Gas</span>
      <span class="brand-rule"></span>
    </div>
    <span class="brand-mark"></span>

    <div class="person">
      <div class="person-name">Derek Fairholm</div>
      <div class="person-role">Plumber</div>
    </div>

    <ul class="contact-list">
      <li class="contact-item">
        <svg class="contact-icon" viewBox="0 0 20 20" aria-hidden="true">
          <rect x="5" y="1.5" width="10" height="17" rx="2" fill="none" stroke="var(--ink-navy)" stroke-width="1.5"/>
          <line x1="8.5" y1="15.5" x2="11.5" y2="15.5" stroke="var(--ink-navy)" stroke-width="1.5"/>
        </svg>
        <span>0418 337 904</span>
      </li>
      <li class="contact-item">
        <svg class="contact-icon" viewBox="0 0 20 20" aria-hidden="true">
          <rect x="1.5" y="4" width="17" height="12" fill="var(--ink-navy)"/>
          <polyline points="1.5,4 10,11 18.5,4" fill="none" stroke="var(--aqua-light)" stroke-width="1.4"/>
        </svg>
        <span>Admin@brightpipeplumbing.example</span>
      </li>
      <li class="contact-item">
        <svg class="contact-icon" viewBox="0 0 20 20" aria-hidden="true">
          <rect x="3.5" y="4" width="13" height="9" fill="none" stroke="var(--ink-navy)" stroke-width="1.5"/>
          <line x1="1" y1="15.5" x2="19" y2="15.5" stroke="var(--ink-navy)" stroke-width="1.8"/>
        </svg>
        <span>www.brightpipeplumbing.example</span>
      </li>
    </ul>
  </section>
</main>
</body>
</html>
```